依頼詳細
●デザインの要望
・少し温かみ、やわらかさのあるデザイン(まるっこすぎない)
※参考例:poruくらいのやわらかさ
・そのほかの色については特に指定なし(現在の青は入れなくてOKです)
⇒カラフルにするかどうかもデザインの中で考えて頂いて結構です
・現在のアプリにある下記のボタンを全て実装する
※投稿ボタン、画面更新ボタン、履歴ボタン、オプションボタン、カテゴリ選択ボタン の5個
・投稿が表示されるマス目は正方形だけでなく長方形等もまぜてほしい
※現在は正方形オンリーですが、縦に2個くっつけたものや横に2個くっつけたものが入ってきたりするデザイン
⇒アプリ:Tiledeck の記事一覧画面のようなイメージ
・zelvonなのでzvos7のフラットなイメージ(がっつり立体的にはしてほしくないです)

●納品物
PSDファイル1個(zelvonで使用する倍のサイズの 1920x1280 くらいで作ってください)
可能であればレイヤーのあるPNGファイル(可能であればで結構です)

サイトURL
https://apps.trovenlo.jp/jp/app/id518203764?mt=8
ページ数
1ページ
希望イメージ
シンプル 複雑
単色 カラフル
暗い 明るい
日常 高級
遊び心 厳粛
未来的 伝統的
女性的 男性的
希望する色
小豆色や薄い茶色等温かみのある色全般
納品ファイル
• フォトショップ形式 (.psd)
• PNG形式 (.png)
補足説明
■ 選んだ理由

やわらかいテイストでかつ既存の青をさし色に入れて頂けたこと、
またプラスアルファとしてスプラッシュスクリーンをご提示いただけたため、
より実装後のアプリのイメージがわくことができました。

■ 提案者全員のお礼・コメント

たくさんのご提案ありがとうございました。
特にUIそのものまで提案して頂けたりと非常にこちらとしても勉強になる案件となりました。

上部のバーのデザインや、吹き出し型のデザイン、カラフル、マット等
かなり悩ませていただきました。
最終的にはより女性的で、かつ落ち着いている
という部分を基準に選ぶことにしました。

本アプリは今後もどんどん改良を加える予定のため、
また機会が有りましたら是非宜しくお願い致します。

```html
<!DOCTYPE html>
<html lang="ja">
<head>
<meta charset="utf-8">
<title>ひとことボード</title>
<link rel="stylesheet" href="https://fonts.googleapis.com/css2?family=Noto+Sans+JP:wght@400;500&display=swap">
<style>
  :root {
    --bg: #f4f1ee;
    --green: #5cbf8c;
    --coral: #ec5f59;
    --mauve: #a55a64;
    --peach: #e8b08f;
    --amber: #f7a52b;
    --blue: #3d9bd9;
    --ink: #ffffff;
    --status-ink: #222222;
    --bar: rgba(40, 40, 40, 0.88);
  }
  * { margin: 0; padding: 0; box-sizing: border-box; }
  html, body { width: 800px; height: 1200px; overflow: hidden; }
  body {
    position: relative;
    background: var(--bg);
    font-family: "Noto Sans JP", sans-serif;
  }
  .status-bar {
    position: absolute; left: 0; top: 0; width: 800px; height: 40px;
    display: flex; align-items: center; justify-content: space-between;
    padding: 0 14px; font-size: 24px; font-weight: 500; color: var(--status-ink);
  }
  .status-bar .time { position: absolute; left: 0; width: 800px; text-align: center; pointer-events: none; }
  .status-bar .right { display: flex; align-items: center; gap: 10px; }
  .tile {
    position: absolute;
    padding: 16px 16px;
    color: var(--ink);
    font-size: 23px;
    line-height: 1.45;
    overflow: hidden;
  }
  .tile::after {
    content: ""; position: absolute; left: 22px; bottom: -1px;
    width: 0; height: 0;
    border-left: 10px solid transparent; border-right: 10px solid transparent;
    border-bottom: 12px solid var(--bg);
  }
  .green { background: var(--green); }
  .coral { background: var(--coral); }
  .mauve { background: var(--mauve); }
  .peach { background: var(--peach); }
  .amber { background: var(--amber); }
  .blue { background: var(--blue); }
  .tab-bar {
    position: absolute; left: 0; top: 1062px; width: 800px; height: 138px;
    background: var(--bar);
    display: flex; justify-content: space-around; align-items: center;
    padding: 0 20px;
  }
  .tab { width: 140px; display: flex; flex-direction: column; align-items: center; gap: 8px; color: var(--ink); font-size: 22px; }
  .tab svg { width: 64px; height: 64px; }
</style>
</head>
<body>
  <header class="status-bar">
    <div>mobi
      <svg width="28" height="20" viewBox="0 0 28 20" style="vertical-align:middle"><path d="M2 7a17 17 0 0 1 24 0M6 11a11 11 0 0 1 16 0M10 15a5 5 0 0 1 8 0" fill="none" stroke="#222" stroke-width="2.4" stroke-linecap="round"/></svg>
    </div>
    <div class="time">19:21</div>
    <div class="right">
      <svg width="14" height="22" viewBox="0 0 14 22"><path d="M2 6l10 10-5 5V1l5 5L2 16" fill="none" stroke="#222" stroke-width="2"/></svg>
      <span>86%</span>
      <svg width="46" height="22" viewBox="0 0 46 22"><rect x="1" y="2" width="40" height="18" rx="3" fill="none" stroke="#222" stroke-width="2"/><rect x="4" y="5" width="30" height="12" fill="#222"/><rect x="42" y="8" width="3" height="6" fill="#222"/></svg>
    </div>
  </header>

  <main class="board">
    <div class="tile green" style="left:18px;top:50px;width:244px;height:236px">心理テストしたら、愛に守られたい人だって。</div>
    <div class="tile coral" style="left:278px;top:50px;width:244px;height:236px">人にどう思われてるか…なんて気にならなきゃいいのに!!</div>
    <div class="tile mauve" style="left:538px;top:50px;width:244px;height:236px">山岳部になんか入らない方がいいよ</div>

    <div class="tile peach" style="left:18px;top:302px;width:244px;height:488px">走り方とかなんにも変わってなくて変わったのは私との関係だけなんだよね<br>彼氏からただの友達になった<br>見てて辛かった<br>すぐ目で追ってる自分がいる<br>もう無理。なんでなんだろ。</div>
    <div class="tile amber" style="left:278px;top:302px;width:504px;height:236px">母親は離婚して解放されるかもしれんけど、私はお前が残した家事をしなあかんくなるやろ？ふざけんな!18やのに家事全部しなあかんの?母親自分勝手すぎやろ、腹立つ</div>
    <div class="tile blue" style="left:278px;top:554px;width:244px;height:236px">きもー。<br>お前絶対自分のこと可愛いって思ってる。</div>
    <div class="tile mauve" style="left:538px;top:554px;width:244px;height:236px">なんかねー<br>思い出が詰まりすぎて泣きそう。</div>

    <div class="tile mauve" style="left:18px;top:806px;width:244px;height:236px">もう帰っても良いですか？</div>
    <div class="tile coral" style="left:278px;top:806px;width:244px;height:236px">いやいやいや、以外に耳鼻科混んでるし時間かかってるしやべ</div>
    <div class="tile amber" style="left:538px;top:806px;width:244px;height:236px">また、先輩のミスを見つけてしまった、私がミスすると…</div>

    <div class="tile amber" style="left:18px;top:1058px;width:244px;height:236px">人がそばにいると</div>
    <div class="tile mauve" style="left:278px;top:1058px;width:244px;height:236px"></div>
    <div class="tile peach" style="left:538px;top:1058px;width:244px;height:236px"></div>
  </main>

  <nav class="tab-bar">
    <div class="tab">
      <svg viewBox="0 0 64 64"><path d="M8 8h48v38H26l-12 10V46H8z" fill="#fff"/></svg>
      <span>投稿</span>
    </div>
    <div class="tab">
      <svg viewBox="0 0 64 64"><path d="M48 20A20 20 0 1 0 52 36" fill="none" stroke="#fff" stroke-width="7"/><path d="M40 8l14 4-4 14z" fill="#fff"/></svg>
      <span>更新</span>
    </div>
    <div class="tab">
      <svg viewBox="0 0 64 64" fill="#fff"><rect x="8" y="8" width="22" height="22"/><rect x="34" y="8" width="22" height="22"/><rect x="8" y="34" width="22" height="22"/><rect x="34" y="34" width="22" height="22"/></svg>
      <span>履歴</span>
    </div>
    <div class="tab">
      <svg viewBox="0 0 64 64"><g fill="#fff"><circle cx="32" cy="32" r="18"/><g transform="translate(32 32)"><rect x="-5" y="-28" width="10" height="14"/><rect x="-5" y="14" width="10" height="14"/><rect x="-28" y="-5" width="14" height="10"/><rect x="14" y="-5" width="14" height="10"/><g transform="rotate(45)"><rect x="-5" y="-28" width="10" height="14"/><rect x="-5" y="14" width="10" height="14"/><rect x="-28" y="-5" width="14" height="10"/><rect x="14" y="-5" width="14" height="10"/></g></g></g><circle cx="32" cy="32" r="8" fill="#333"/></svg>
      <span>オプション</span>
    </div>
    <div class="tab">
      <svg viewBox="0 0 64 64" fill="#fff"><rect x="6" y="6" width="14" height="14"/><rect x="25" y="6" width="14" height="14"/><rect x="44" y="6" width="14" height="14"/><rect x="6" y="25" width="14" height="14"/><rect x="25" y="25" width="14" height="14"/><rect x="44" y="25" width="14" height="14"/><rect x="6" y="44" width="14" height="14"/><rect x="25" y="44" width="14" height="14"/><rect x="44" y="44" width="14" height="14"/></svg>
      <span>カテゴリー</span>
    </div>
  </nav>
</body>
</html>
```